Front & Back cover design for timber flooring brochure - A4 size

I need a design for the front and back cover of an A4 sized brochure for a timber and concrete flooring company called "Kestrel Row Floors". The front cover should include the logo (attached), and an image + tagline for each of the three products/services that they offer which are:

1. Timber Flooring
2. Concrete Grinding & Sealing
3. Floor sanding (i have attached a photo for each of these three - however feel free to use other images if you feel they are better).

The back cover should be simple, perhaps just a continuation of the colour or graphic scheme on the front with the company contact details at the bottom.

Industry/Entity Type

Flooring

Requirements
Must have
• front cover has to have the logo with an image and text of the 3 services described. You can use the images attached or your own.

```html
<!DOCTYPE html>
<html lang="en">
<head>
<meta charset="utf-8">
<title>Kestrel Row Floors – Brochure Cover</title>
<link rel="stylesheet" href="https://fonts.googleapis.com/css2?family=Marcellus+SC&display=swap">
<style>
  :root {
    --wood-deep: #5e1410;
    --wood-mid: #8c2a1b;
    --wood-warm: #a8461f;
    --swoosh: #ffffff;
    --brand: #7a4a1c;
    --silver: #e6e6e6;
    --silver-dark: #9c9c9c;
    --ink-light: #f1e6dc;
    --seam: #c9a79a;
    --faint: rgba(60,10,8,.26);
  }
  * { margin: 0; padding: 0; box-sizing: border-box; }
  html, body { width: 1200px; height: 849px; overflow: hidden; background: #ffffff; }
  .spread { position: relative; width: 1200px; height: 849px; overflow: hidden; font-family: "Marcellus SC", serif; }

  .floor-photo {
    position: absolute; inset: 0;
    background:
      radial-gradient(ellipse 90px 160px at 20px 420px, rgba(214,120,40,.55), transparent 70%),
      radial-gradient(ellipse 90px 160px at 1150px 500px, rgba(214,120,40,.45), transparent 70%),
      radial-gradient(ellipse 400px 300px at 300px 500px, var(--wood-mid), transparent 80%),
      radial-gradient(ellipse 400px 300px at 900px 420px, var(--wood-mid), transparent 80%),
      linear-gradient(180deg, var(--wood-warm) 0%, var(--wood-mid) 35%, var(--wood-deep) 100%);
  }
  .page-seam { position: absolute; left: 600px; top: 0; width: 1px; height: 849px; background: var(--seam); }
  .swooshes { position: absolute; inset: 0; }

  .faint-name { position: absolute; color: var(--faint); white-space: nowrap; font-weight: 400; }
  .faint-name.back-top { left: 150px; top: 38px; font-size: 42px; }
  .faint-name.back-low { left: 132px; top: 258px; font-size: 42px; }
  .faint-name.front-diag { left: 620px; top: 392px; width: 560px; text-align: center; font-size: 50px; transform: rotate(-24deg); }

  .tile-grid { position: absolute; display: grid; grid-template-columns: repeat(4, 1fr); }
  .tile-grid span { display: block; box-shadow: inset 0 0 0 2px rgba(255,255,255,.25), inset 0 0 0 3px rgba(0,0,0,.25), 2px 3px 4px rgba(0,0,0,.45); }
  .tile-grid.small { left: 188px; top: 103px; width: 94px; height: 140px; gap: 2px; grid-template-rows: repeat(6, 1fr); opacity: .85; }
  .tile-grid.large { left: 771px; top: 231px; width: 258px; height: 361px; gap: 7px; grid-template-rows: repeat(6, 1fr); }

  .t1 { background: linear-gradient(135deg,#7a4428,#5a2e1b); }
  .t2 { background: linear-gradient(135deg,#8e5233,#6b3822); }
  .t3 { background: linear-gradient(135deg,#8a5a38,#6e4227); }
  .t4 { background: linear-gradient(135deg,#955d36,#74442a); }
  .t5 { background: linear-gradient(135deg,#5c2c1c,#3f1c12); }
  .t6 { background: linear-gradient(135deg,#e3c8ad,#cfae90); }
  .t7 { background: linear-gradient(135deg,#f0d6b1,#dcbd92); }
  .t8 { background: linear-gradient(135deg,#e2c5a7,#cfa986); }
  .t9 { background: linear-gradient(135deg,#9a6430,#7d4d22); }
  .t10 { background: linear-gradient(135deg,#8c4d2c,#6d3820); }
  .t11 { background: linear-gradient(135deg,#95603a,#744627); }
  .t12 { background: linear-gradient(135deg,#6a3823,#4d2617); }
  .t13 { background: linear-gradient(135deg,#a07552,#7f5738); }
  .t14 { background: linear-gradient(135deg,#e0b894,#c9977a); }
  .t15 { background: linear-gradient(135deg,#b07a4e,#925f39); }
  .t16 { background: linear-gradient(135deg,#6e3d24,#522b19); }
  .t17 { background: linear-gradient(135deg,#c08a48,#a06e34); }
  .t18 { background: linear-gradient(135deg,#c89456,#a97740); }
  .t19 { background: linear-gradient(135deg,#d6ae78,#b98f5c); }
  .t20 { background: linear-gradient(135deg,#9c6a3a,#7d5029); }
  .t21 { background: linear-gradient(135deg,#6a3c26,#4e2a19); }
  .t22 { background: linear-gradient(135deg,#8a4a2c,#6a361f); }
  .t23 { background: linear-gradient(135deg,#3d1c12,#2a120b); }
  .t24 { background: linear-gradient(135deg,#8e5634,#6c3e24); }

  .corner-tile { position: absolute; width: 56px; height: 56px; box-shadow: inset 0 0 0 2px rgba(255,255,255,.25), 2px 3px 4px rgba(0,0,0,.45); }
  .corner-tile.a { left: 663px; top: 731px; background: linear-gradient(135deg,#a86a36,#82502a); }
  .corner-tile.b { left: 603px; top: 789px; background: linear-gradient(135deg,#9a5e30,#774624); }
  .corner-tile.c { left: 1081px; top: 731px; background: linear-gradient(135deg,#9a6234,#764826); }
  .corner-tile.d { left: 1141px; top: 789px; background: linear-gradient(135deg,#a26a3a,#7e5029); }

  .brand-name { position: absolute; color: var(--brand); white-space: nowrap; text-align: center; font-weight: 400; }
  .brand-name.front { left: 660px; top: 52px; width: 480px; font-size: 40px; line-height: 56px; }
  .brand-name.back { left: 140px; top: 602px; width: 230px; font-size: 19px; line-height: 26px; }

  .services { position: absolute; list-style: none; text-align: center; }
  .services.back { left: 80px; top: 334px; width: 440px; font-size: 20px; line-height: 31px; letter-spacing: 1.4px; color: var(--ink-light); text-shadow: 1px 1px 2px rgba(0,0,0,.5); }
  .services.front { left: 605px; top: 628px; width: 590px; font-size: 31px; line-height: 47px; letter-spacing: 1.6px; color: var(--silver); text-shadow: 1px 1px 0 var(--silver-dark), 2px 3px 3px rgba(0,0,0,.6); }

  .contact { position: absolute; left: 135px; top: 668px; font-style: normal; color: var(--ink-light); font-size: 8.5px; line-height: 11px; letter-spacing: 1px; }
  .contact h2 { font-weight: 400; font-size: 10.5px; letter-spacing: 1.2px; margin-bottom: 6px; }
  .contact p { margin-bottom: 10px; }
</style>
</head>
<body>
<main class="spread">
  <div class="floor-photo" role="img" aria-label="Polished red-brown timber floor with warm light reflections"></div>

  <svg class="swooshes" width="1200" height="849" viewBox="0 0 1200 849" aria-hidden="true">
    <path fill="var(--swoosh)" d="M285,157 C400,138 520,128 680,124 C880,120 1060,140 1140,200 C1145,120 1165,80 1200,62 L1200,14 C1100,16 960,10 880,0 L620,0 C605,45 565,80 480,108 C420,128 340,148 285,157 Z"/>
    <path fill="var(--swoosh)" d="M20,512 C120,560 200,590 520,580 C400,600 360,640 470,720 C380,680 300,650 200,645 C120,642 50,648 0,652 L0,640 C60,620 120,580 20,512 Z"/>
  </svg>
  <div class="page-seam"></div>

  <section class="back-cover">
    <div class="faint-name back-top" aria-hidden="true">Kestrel Row</div>
    <div class="faint-name back-low" aria-hidden="true">Floors</div>
    <div class="tile-grid small" role="img" aria-label="Grid of timber flooring samples">
      <span class="t1"></span><span class="t2"></span><span class="t3"></span><span class="t4"></span>
      <span class="t5"></span><span class="t6"></span><span class="t7"></span><span class="t8"></span>
      <span class="t9"></span><span class="t10"></span><span class="t11"></span><span class="t12"></span>
      <span class="t13"></span><span class="t14"></span><span class="t15"></span><span class="t16"></span>
      <span class="t17"></span><span class="t18"></span><span class="t19"></span><span class="t20"></span>
      <span class="t21"></span><span class="t22"></span><span class="t23"></span><span class="t24"></span>
    </div>
    <ul class="services back">
      <li>Timber Flooring</li>
      <li>Concrete Grinding &amp; Sealing</li>
      <li>Floor sanding</li>
    </ul>
    <div class="brand-name back">Kestrel Row Floors</div>
    <address class="contact">
      <h2>Your Address</h2>
      <p>Justo sed augue ultricies ut bibendum +<br>ante facilisis. Integer vehicula<br>nisl nec tellus tempor auctor. Ut eu<br>mi sem. Nunc vel</p>
      <p>Ph.: 123 456 7890<br>&nbsp;&nbsp;&nbsp;&nbsp;&nbsp;&nbsp;&nbsp;&nbsp;123 456 7890</p>
      <p>amet lectus vel neque</p>
    </address>
  </section>

  <section class="front-cover">
    <div class="faint-name front-diag" aria-hidden="true">Kestrel Row Floors</div>
    <div class="brand-name front">Kestrel Row Floors</div>
    <div class="tile-grid large" role="img" aria-label="Grid of timber flooring samples in light to dark tones">
      <span class="t1"></span><span class="t2"></span><span class="t3"></span><span class="t4"></span>
      <span class="t5"></span><span class="t6"></span><span class="t7"></span><span class="t8"></span>
      <span class="t9"></span><span class="t10"></span><span class="t11"></span><span class="t12"></span>
      <span class="t13"></span><span class="t14"></span><span class="t15"></span><span class="t16"></span>
      <span class="t17"></span><span class="t18"></span><span class="t19"></span><span class="t20"></span>
      <span class="t21"></span><span class="t22"></span><span class="t23"></span><span class="t24"></span>
    </div>
    <ul class="services front">
      <li>Timber Flooring</li>
      <li>Concrete Grinding &amp; Sealing</li>
      <li>Floor sanding</li>
    </ul>
    <div class="corner-tile a" role="img" aria-label="Timber sample"></div>
    <div class="corner-tile b" role="img" aria-label="Timber sample"></div>
    <div class="corner-tile c" role="img" aria-label="Timber sample"></div>
    <div class="corner-tile d" role="img" aria-label="Timber sample"></div>
  </section>
</main>
</body>
</html>
```